Calendar Ad / Flyer

Our law firm needs a calendar ad to place in a local calendar.
THE DEADLINE IS THIS THURSDAY 06/28/2018.

Attached is the ad used in last years calendar. A few notes on this...
**. This is by no means the model to follow.
Please be creative and do what makes more sense marketing wise.
1. Need to update the color scheme which corresponds to the new website at morvanlegal.net
2. The "MORVAN LEGAL | STANDING FIRM FOR YOUR FUTURE" should be put at the top and made larger
3. "KNOWN AND TRUSTED IN OUR COMMUNITY FOR OVER 21 YEARS" should be changed to "KNOWN AND TRUSTED IN OUR COMMUNITY FOR OVER 22 YEARS"
4. "Dorian K. Morvan, Esq." should be made larger and better positioned.
5. Under the list of practices, it should be changed to have:
"Personal Injury, Legal Malpractice, Unlicensed Contractors, Medical Malpractice, Civil Litigation"
6. Contact information (i.e. contact number, website, and address) should be better positioned
7. Placement of endorsement logos should stand out more.
8. New picture of head attorney is attached.

Last but not least... Give it your best shot!

```html
<!DOCTYPE html>
<html lang="en">
<head>
<meta charset="utf-8">
<title>Morvan Legal – Calendar Ad</title>
<link rel="stylesheet" href="https://fonts.googleapis.com/css2?family=Libre+Baskerville:wght@400;700&family=Montserrat:wght@400;500;600&display=swap">
<style>
  :root {
    --ink-dark: #1f1f20;
    --ink-mid: #2c2c2e;
    --strip-grey: #4a4b4f;
    --gold: #c8a572;
    --tan-band: #c9a46e;
    --name-grey: #46484d;
    --text-dark: #3a3b3f;
    --tagline: #e4e0da;
    --white: #ffffff;
    --photo-warm: #b9a48c;
    --photo-cool: #8d8f94;
  }
  * { box-sizing: border-box; margin: 0; padding: 0; }
  html, body { width: 1200px; height: 900px; overflow: hidden; background: var(--white); }
  .ad { position: relative; width: 1200px; height: 900px; overflow: hidden; background: var(--white); font-family: "Libre Baskerville", Georgia, serif; }

  .hero { position: absolute; left: 0; top: 0; width: 1200px; height: 417px;
    background: linear-gradient(160deg, #3a3a3c 0%, var(--ink-mid) 35%, var(--ink-dark) 100%); }
  .grey-strip { position: absolute; left: 0; top: 417px; width: 1060px; height: 17px; background: var(--strip-grey); }

  .brand { position: absolute; left: 88px; top: 134px; width: 524px; text-align: center; }
  .brand-name { display: flex; align-items: center; justify-content: center; gap: 14px; white-space: nowrap;
    font-family: "Montserrat", Arial, sans-serif; font-weight: 500; font-size: 44px; letter-spacing: 5px; color: var(--gold); line-height: 1; }
  .brand-mark { flex: none; width: 24px; height: 24px; background: var(--gold); }
  .brand-tagline { margin-top: 12px; white-space: nowrap; font-family: "Montserrat", Arial, sans-serif; font-size: 17px; letter-spacing: 1.5px; color: var(--tagline); line-height: 1; }

  .headline { position: absolute; left: 88px; top: 252px; color: var(--white); font-size: 30px; font-weight: 400; line-height: 1.2; white-space: nowrap; }
  .headline-years { display: block; color: var(--gold); font-size: 38px; font-weight: 400; margin-top: 4px; }

  .name-band { position: absolute; left: 0; top: 434px; width: 1200px; height: 122px; }
  .attorney-name { position: absolute; left: 86px; top: 24px; font-size: 60px; font-weight: 700; color: var(--name-grey); white-space: nowrap; line-height: 1.2; }

  .practice-band { position: absolute; left: 0; top: 556px; width: 1200px; height: 130px; background: var(--tan-band); }
  .practice-list { position: absolute; top: 14px; list-style: none; color: var(--white); font-size: 24px; line-height: 1.15; white-space: nowrap; }
  .practice-list li::before { content: "•"; margin-right: 16px; }
  .practice-list.col-a { left: 92px; }
  .practice-list.col-b { left: 512px; }

  .contact { position: absolute; left: 92px; top: 703px; font-family: "Montserrat", Arial, sans-serif; color: var(--text-dark); white-space: nowrap; }
  .contact-line { display: flex; gap: 86px; font-size: 29px; font-weight: 600; line-height: 1.1; }
  .contact-address { margin-top: 8px; font-size: 17px; font-weight: 500; }

  .endorsements { position: absolute; left: 83px; top: 778px; display: flex; align-items: center; gap: 40px; }
  .badge { flex: none; }
  .badge.round { width: 92px; height: 92px; border-radius: 50%; background: #7a1d1d; }
  .badge.wordmark { width: 110px; height: 74px; border-radius: 6px; background: #d9b160; }
  .badge.stars { width: 124px; height: 84px; border-radius: 6px; background: #c8102e; }
  .badge.shield { width: 104px; height: 98px; border-radius: 6px; background: #1d5f8f; }
  .badge.rating { width: 98px; height: 98px; border-radius: 50%; background: #2b8fd0; }

  .photo-bottom { position: absolute; left: 853px; top: 682px; width: 298px; height: 218px;
    background: linear-gradient(180deg, #f2f2f2 0%, #d8d4d0 45%, var(--photo-cool) 100%); }

  .photo-frame { position: absolute; left: 737px; top: 180px; width: 540px; height: 472px;
    transform-origin: 0 0; transform: rotate(-30deg); background: var(--white); padding: 12px;
    box-shadow: 4px 8px 14px rgba(0,0,0,0.35); }
  .photo-frame-inner { width: 100%; height: 100%;
    background: linear-gradient(135deg, #d9c8b2 0%, var(--photo-warm) 40%, var(--photo-cool) 100%); }
</style>
</head>
<body>
<main class="ad">
  <section class="hero" role="img" aria-label="Dark city skyline photograph behind the firm name"></section>
  <div class="grey-strip"></div>

  <header class="brand">
    <div class="brand-name"><span class="brand-mark"></span>MORVAN LEGAL</div>
    <div class="brand-tagline">STANDING FIRM FOR YOUR FUTURE</div>
  </header>

  <h2 class="headline">Known and Trusted in Our Community<span class="headline-years">For Over 22 Years</span></h2>

  <section class="name-band">
    <h1 class="attorney-name">Dorian K. Morvan, Esq.</h1>
  </section>

  <section class="practice-band">
    <ul class="practice-list col-a">
      <li>Personal Injury,</li>
      <li>Legal Malpractice,</li>
      <li>Unlicensed Contractors,</li>
    </ul>
    <ul class="practice-list col-b">
      <li>Medical Malpractice</li>
      <li>Civil Litigation</li>
    </ul>
  </section>

  <section class="contact">
    <div class="contact-line"><span class="contact-phone">(888) 555-0142</span><span class="contact-web">www.morvanlegal.net</span></div>
    <div class="contact-address">2180, Corbel Ave, Suite 410, Westlake, CA 90361</div>
  </section>

  <section class="endorsements" aria-label="Endorsements">
    <div class="badge round" role="img" aria-label="Advocates forum seal"></div>
    <div class="badge wordmark" role="img" aria-label="Attorney listing badge"></div>
    <div class="badge stars" role="img" aria-label="Five-star review badge"></div>
    <div class="badge shield" role="img" aria-label="Accredited business badge"></div>
    <div class="badge rating" role="img" aria-label="Top attorney rating badge"></div>
  </section>

  <div class="photo-bottom" role="img" aria-label="Portrait photo of the attorney, head and shoulders"></div>

  <div class="photo-frame">
    <div class="photo-frame-inner" role="img" aria-label="Framed photo of the attorney in a grey suit in his office"></div>
  </div>
</main>
</body>
</html>
```